Riverbend Haven Home Care-Flyer for Patients

Our Home Health Care Agency, Riverbend Haven Home Care, is seeking a flyer to advertise our services. We would like our flyer to convey professionalism, classiness and sophistication. We want our agency to come across as one that is well-established and recognized as being first-rate within the field.

We also want to appear original; we want to stand out.

Our theme colors, blue and green, from our logo should be incorporated into the flyer's design (refer below).

The top of the page should say (in a clear, bold font)-Seeking Care for your Loved One?

Our Logo, followed by our slogan, "Let Your Neighbors Look After You", should be in the center. (This should make it appear as if our agency is the obvious solution to the consumer's quest in finding suitable care for their family member). This should be in a big font.
Below that, our agency's services should be listed in a very noticeable font...yet smaller than what's written above that.
The text should read:
Our Services Include:
*Experienced Certified Home Health Aides/ Live In Home Health Aides/Companions
*Nursing Services
*Alzheimer’s and Dementia Care
*Respite Care
*Postoperative Care
*Post Rehabilitation Care
*Running Errands
*Light Housekeeping
*Assistance with Bathing, Feeding and Grooming
*Meal Preparation
*Laundry and Linen Washing
*Mail and Bill Organization
*Medication Management
*Accompanying to Doctor’s Appointments
*And much more!
Below that, in a smaller, yet noticeable font:
As seasoned professionals, we know how to help our clients navigate and fulfill their various health care needs. Your Community is here to help you get the care that you deserve.
Call Riverbend Haven Home Care today to learn more about our first-rate services!
Below that, in a larger font, our phone number, website, our e-mail address.
*Out contact information will be provided to the project’s winner*.

*Pictures of Caregivers helping elderly patient should be included in the advertisement as well. *

We provided advertisements of other Home Health Care Agencies attached below to use as a reference. Once again, while we are aiming for a similar idea; however, our goal is to stand out as the community's premiere home health care agency, the one that they want to choose. We want to be original as well!

Size: Standard Computer Paper Size. 8.5” x 11”.

Feel free to utilize your creative, designer flair!
We look forward to seeing the results!
Good luck!

Industry/Entity Type

Home Health Care

Font styles to use
Sans Serif

Requirements
Must have
• Refer above.
Nice to have
• Refer to attachment below to see how other home health care agencies advertise. While we are aiming for a similar idea, we would like to incorporate our logo, slogan and colors to make this flyer more unique and stand out. We would like to appear original.

```html
<!DOCTYPE html>
<html lang="en">
<head>
<meta charset="utf-8">
<title>Riverbend Haven Home Care – Flyer</title>
<link href="https://fonts.googleapis.com/css2?family=Montserrat:wght@400;500;600;700;800;900&display=swap" rel="stylesheet">
<style>
:root{
  --blue:#0b4a92;
  --blue-deep:#083b78;
  --green:#7dc242;
  --green-dark:#5a9a2a;
  --grey-panel:#efefef;
  --page:#e6e6e6;
  --ink:#2b2b2b;
  --white:#ffffff;
}
*{margin:0;padding:0;box-sizing:border-box}
html,body{width:1200px;height:2400px;overflow:hidden;background:var(--page);font-family:"Montserrat",Arial,sans-serif}
.flyer{position:absolute;left:40px;top:474px;width:1120px;height:1451px;background:var(--white);overflow:hidden;box-shadow:0 6px 24px rgba(0,0,0,.12)}

/* brand block */
.brand{position:absolute;left:55px;top:70px;width:475px;text-align:center;color:var(--blue)}
.brand-dot{width:150px;height:150px;border-radius:50%;border:14px solid var(--green);margin:0 auto 34px}
.brand-name{font-weight:800;font-size:42px;line-height:1.08;letter-spacing:.5px;color:var(--blue)}
.brand-slogan{margin-top:14px;font-weight:700;font-size:14px;letter-spacing:2.4px;white-space:nowrap;color:var(--blue)}

/* hero photo */
.hero{position:absolute;left:580px;top:-60px;width:560px;height:540px}

/* headline band */
.headline-band{position:absolute;left:0;top:474px;width:100%;height:151px;background:var(--blue);text-align:center;color:var(--white)}
.headline{margin-top:28px;font-size:48px;font-weight:500;letter-spacing:.3px;line-height:1}
.headline .accent{color:var(--green);font-weight:900}
.headline .strong{font-weight:900}
.subline{margin-top:16px;font-size:33px;font-weight:400;letter-spacing:.2px}

/* services */
.services-panel{position:absolute;left:0;top:680px;width:100%;height:409px;background:var(--grey-panel)}
.services-tab{position:absolute;left:48px;top:660px;width:447px;height:57px}
.services-tab span{position:absolute;left:28px;top:8px;font-size:43px;font-weight:800;color:var(--white);letter-spacing:.5px;line-height:1}
.service{position:absolute;display:flex;align-items:flex-start;gap:16px;font-size:19.5px;font-weight:600;color:var(--ink);line-height:1.22;letter-spacing:.2px}
.service svg{flex:none;width:48px;height:48px;margin-top:-12px}
.more-btn{position:absolute;left:732px;top:1012px;padding:4px 10px;background:var(--blue);color:var(--white);border-radius:5px;font-size:19.5px;font-weight:700}

/* about */
.hands{position:absolute;left:575px;top:1092px;width:545px;height:251px}
.about{position:absolute;left:51px;top:1146px;width:530px;font-size:19.5px;line-height:1.13;color:#3a3a3a;font-weight:400}
.cta{position:absolute;left:48px;top:1252px;width:525px;height:74px;background:var(--blue);border-radius:6px;color:var(--white);font-size:20.5px;font-weight:700;line-height:1.12;padding:13px 18px}

/* footer */
.footer{position:absolute;left:0;top:1340px;width:1120px;height:111px}
.contact{display:flex;align-items:center;gap:10px;font-weight:700;line-height:1;white-space:nowrap}
.contact-web{position:absolute;left:55px;top:1388px;font-size:25px;color:var(--ink)}
.contact-row{position:absolute;left:515px;top:1383px;width:580px;height:40px;display:flex;align-items:center;gap:22px}
.contact-phone{font-size:32px;color:var(--white)}
.contact-mail{font-size:24px;color:var(--white);font-weight:600}
</style>
</head>
<body>
<main class="flyer">

  <section class="brand">
    <div class="brand-dot"></div>
    <div class="brand-name">RIVERBEND HAVEN<br>HOME CARE</div>
    <div class="brand-slogan">LET YOUR NEIGHBORS LOOK AFTER YOU</div>
  </section>

  <svg class="hero" viewBox="0 0 560 540">
    <defs>
      <linearGradient id="photoTone" x1="0" y1="0" x2="1" y2="1">
        <stop offset="0" stop-color="#b9c9b0"/>
        <stop offset=".5" stop-color="#e7c7c0"/>
        <stop offset="1" stop-color="#7fa9d6"/>
      </linearGradient>
    </defs>
    <path d="M52 60 A 262 262 0 0 0 230 530" fill="none" stroke="var(--green)" stroke-width="14"/>
    <path d="M420 10 A 262 262 0 0 1 560 120" fill="none" stroke="var(--green)" stroke-width="10"/>
    <path d="M80 40 A 250 250 0 0 0 170 500" fill="none" stroke="var(--blue)" stroke-width="6"/>
    <circle cx="286" cy="271" r="250" fill="url(#photoTone)" role="img" aria-label="Photo: a smiling caregiver in blue scrubs with her hands on the shoulders of an elderly woman outdoors"/>
  </svg>

  <section class="headline-band">
    <p class="headline"><span class="accent">SEEKING CARE</span> FOR YOU <span class="strong">LOVED ONE?</span></p>
    <p class="subline">LET YOUR NEIGHBORS LOOK AFTER YOU</p>
  </section>

  <div class="services-panel"></div>
  <svg class="services-tab" viewBox="0 0 447 57">
    <path d="M395 0 H447 V18 A14 14 0 0 0 433 18 L395 18Z" fill="var(--green-dark)"/>
    <path d="M0 0 H430 Q410 10 400 57 H0Z" fill="var(--green)"/>
  </svg>
  <div class="services-tab"><span>OUR SERVICES</span></div>

  <svg width="0" height="0" style="position:absolute">
    <symbol id="svc-icon" viewBox="0 0 48 48">
      <circle cx="24" cy="24" r="22" fill="var(--white)" stroke="var(--green)" stroke-width="2.5"/>
      <circle cx="24" cy="24" r="16.5" fill="none" stroke="#9a9a9a" stroke-width="1" stroke-dasharray="2 2"/>
      <path d="M16 24.5 L21.5 30 L32 18.5" fill="none" stroke="var(--blue)" stroke-width="2.6" stroke-linecap="round" stroke-linejoin="round"/>
    </symbol>
  </svg>

  <div class="service" style="left:49px;top:752px"><svg><use href="#svc-icon"/></svg><span>Experienced Certified Home<br>Health Aides/ Live In Home<br>Health Aides/Companions</span></div>
  <div class="service" style="left:49px;top:848px"><svg><use href="#svc-icon"/></svg><span>Nursing Services</span></div>
  <div class="service" style="left:49px;top:897px"><svg><use href="#svc-icon"/></svg><span>Alzheimer’s and<br>Dementia Care</span></div>
  <div class="service" style="left:49px;top:966px"><svg><use href="#svc-icon"/></svg><span>Respite Care</span></div>
  <div class="service" style="left:49px;top:1014px"><svg><use href="#svc-icon"/></svg><span>Postoperative Care</span></div>

  <div class="service" style="left:409px;top:752px"><svg><use href="#svc-icon"/></svg><span>Post Rehabilitation Care</span></div>
  <div class="service" style="left:409px;top:811px"><svg><use href="#svc-icon"/></svg><span>Running Errands</span></div>
  <div class="service" style="left:409px;top:869px"><svg><use href="#svc-icon"/></svg><span>Light Housekeeping</span></div>
  <div class="service" style="left:409px;top:929px"><svg><use href="#svc-icon"/></svg><span>Assistance with Bathing<br>Feeding and Grooming</span></div>
  <div class="service" style="left:409px;top:1016px"><svg><use href="#svc-icon"/></svg><span>Meal Preparation</span></div>

  <div class="service" style="left:729px;top:752px"><svg><use href="#svc-icon"/></svg><span>Laundry and Linen Washing</span></div>
  <div class="service" style="left:729px;top:811px"><svg><use href="#svc-icon"/></svg><span>Mail and Bill Organization</span></div>
  <div class="service" style="left:729px;top:869px"><svg><use href="#svc-icon"/></svg><span>Medication Management</span></div>
  <div class="service" style="left:729px;top:929px"><svg><use href="#svc-icon"/></svg><span>Accompanying to Doctor’s<br>Appointments</span></div>
  <div class="more-btn">And much more!</div>

  <svg class="hands" viewBox="0 0 545 251" role="img" aria-label="Black and white photo: a caregiver's hands gently holding an elderly person's hand">
    <defs>
      <linearGradient id="handsTone" x1="0" y1="0" x2="1" y2="0">
        <stop offset="0" stop-color="#ffffff" stop-opacity="0"/>
        <stop offset=".35" stop-color="#d6d6d6"/>
        <stop offset="1" stop-color="#9c9c9c"/>
      </linearGradient>
    </defs>
    <rect width="545" height="251" fill="url(#handsTone)"/>
  </svg>

  <p class="about">As seasoned professionals, we know how to help our clients navigate and fulfill their various health care needs. Your Community is here to help you get the care that you deserve.</p>
  <div class="cta">Call Riverbend Haven Home Care today to learn more about our first-rate services!</div>

  <svg class="footer" viewBox="0 0 1120 111">
    <rect x="0" y="0" width="1120" height="6" fill="var(--white)"/>
    <path d="M340 111 C 400 60, 420 22, 500 6 H1120 V111Z" fill="var(--green)"/>
    <path d="M340 111 C 380 70, 400 40, 450 20 C 400 50, 390 80, 370 111Z" fill="var(--blue)"/>
    <path d="M0 100 H380 L372 111 H0Z" fill="var(--green)"/>
    <path d="M0 103 H8 V111 H0Z" fill="var(--blue)"/>
  </svg>

  <div class="contact contact-web">
    <svg width="22" height="22" viewBox="0 0 24 24"><circle cx="12" cy="12" r="10" fill="none" stroke="var(--blue)" stroke-width="2"/><ellipse cx="12" cy="12" rx="4.5" ry="10" fill="none" stroke="var(--blue)" stroke-width="1.6"/><path d="M2 12H22M4 7H20M4 17H20" stroke="var(--blue)" stroke-width="1.4"/></svg>
    <span>www.rbhaven.com</span>
  </div>
  <div class="contact-row">
    <div class="contact contact-phone">
      <svg width="26" height="26" viewBox="0 0 24 24"><path d="M6.6 10.8a15 15 0 0 0 6.6 6.6l2.2-2.2c.3-.3.7-.4 1-.2 1.1.4 2.3.6 3.6.6.6 0 1 .4 1 1V20c0 .6-.4 1-1 1C10.6 21 3 13.4 3 4c0-.6.4-1 1-1h3.5c.6 0 1 .4 1 1 0 1.3.2 2.5.6 3.6.1.3 0 .7-.2 1Z" fill="var(--blue)"/></svg>
      <span>555.014.2287</span>
    </div>
    <div class="contact contact-mail">
      <svg width="24" height="18" viewBox="0 0 24 18"><rect x="1" y="1" width="22" height="16" fill="none" stroke="var(--blue)" stroke-width="2"/><path d="M1 1 L12 10 L23 1" fill="none" stroke="var(--blue)" stroke-width="2"/></svg>
      <span>care@rbhaven.com</span>
    </div>
  </div>

</main>
</body>
</html>
```